Cruise & Resort Travel Redemption Vouchers

Need to have all of these pages completely re-done. These designs are horrible and need to look much more professional. The individual vouchers like the "maple grove laugh house" & Copper Lantern supper can look similar to the design on their websites.
Maple grove link
http://laughhousemg.com/
Copper Lantern Supper
http://www.copper-lantern.com/
Please do something with the tiny anchors all over the place. Or just get rid of them.
Does not need to be over the top design heavy...just professional and simple with small doses of vacation added.
Updates
get rid of the stupid anchors all over the place.
Target Market(s)
35-60
Industry/Entity Type
Club
Requirements
Must have
- All pages done.
The company logo on the pages,found here.
http://sunbreakgetaways.com/
The Abbreviation is T.L.R

```html
<!DOCTYPE html>
<html lang="en">
<head>
<meta charset="utf-8">
<title>Attraction Ticket Vouchers</title>
<link href="https://fonts.googleapis.com/css2?family=Arimo:ital,wght@0,400;0,700;1,400;1,700&family=Roboto+Condensed:wght@400;500&display=swap" rel="stylesheet">
<style>
:root{
  --page:#ece7df;
  --sky:#1fb1ea;
  --sky-light:#bfe8fa;
  --sky-deep:#0a8fc8;
  --bar:#7f8184;
  --ink:#1a1a1a;
  --navy:#0a2a66;
  --rule:#333;
  --box-line:#7a7a7a;
}
*{box-sizing:border-box;margin:0;padding:0}
html,body{width:943px;height:1200px;overflow:hidden}
body{background:var(--page);font-family:"Arimo",Arial,sans-serif;color:var(--ink);position:relative}
.sheet{position:absolute;left:57px;top:63px;width:829px;height:1070px;box-shadow:0 2px 6px rgba(0,0,0,.25)}
.voucher{position:relative;width:829px;height:535px;overflow:hidden;
  background:linear-gradient(180deg,var(--sky-light) 0,#fff 9%,#fff 82%,var(--sky-light) 88%,var(--sky) 100%);
  border-bottom:1px dashed #9bcbe3}
.wave{position:absolute;top:0;bottom:0;width:70px}
.wave-left{left:0;background:linear-gradient(90deg,var(--sky) 0,var(--sky-light) 55%,rgba(255,255,255,0) 100%)}
.wave-right{right:0;background:linear-gradient(270deg,var(--sky) 0,var(--sky-light) 55%,rgba(255,255,255,0) 100%)}
.brand-tab{position:absolute;left:309px;top:0;width:210px;height:62px;background:var(--sky-deep);z-index:2;
  border-radius:0 0 105px 105px / 0 0 62px 62px;display:flex;align-items:center;justify-content:center;gap:6px;padding-bottom:6px}
.brand-tab .dot{width:9px;height:9px;border-radius:50%;background:#fff}
.brand-tab .name{color:#fff;font-size:13px;font-weight:700;white-space:nowrap}
.panel{position:absolute;top:57px;border:1px solid var(--box-line);background:rgba(255,255,255,.92);padding:16px 18px 0}
.panel-left{left:15px;width:388px;height:403px}
.panel-right{left:416px;width:367px;height:400px}
.bar{background:var(--bar);color:#fff;font-family:"Roboto Condensed","Arial Narrow",sans-serif;font-size:14px;
  text-align:center;height:24px;line-height:24px;text-transform:uppercase;letter-spacing:.3px}
.panel-left .bar{margin:0 10px 0 62px}
.panel-right .bar{margin:0 -6px}
.center{text-align:center;font-size:12.5px;line-height:16px}
.offer{font-size:12px;line-height:15px;margin-top:7px;padding-left:52px}
.note{font-size:9px;font-style:italic;font-weight:700;text-align:center;line-height:11px;margin-top:4px;padding-left:52px}
.package{display:flex;align-items:center;justify-content:center;gap:8px;font-size:13px;margin:8px 0 8px 52px}
.package .box{width:150px;height:30px;border:1px solid #555;background:#fff}
.field{display:flex;align-items:flex-end;font-size:12.5px;height:25px}
.field .line{flex:1;border-bottom:1px solid var(--rule);margin-left:2px;height:14px}
.field .short{flex:none;width:80px}
.field .tiny{flex:none;width:40px}
.fields{margin-top:6px}
.interest{display:flex;gap:10px;margin-top:8px}
.attraction-mark{width:100px;height:64px;display:flex;align-items:center;justify-content:center;text-align:center;font-size:12px;font-weight:700;color:var(--sky-deep);line-height:14px}
.interest-copy{flex:1}
.interest-copy .title{font-size:12.5px;font-weight:700;margin-top:6px}
.interest-copy .line{border-bottom:1px solid var(--rule);height:24px}
.interest-copy .hint{font-size:7.5px;font-style:italic;font-weight:700;text-align:center}
.extra{font-size:11px;display:flex;align-items:flex-end}
.extra .line{flex:1;border-bottom:1px solid var(--rule);height:12px}
.extra-line{border-bottom:1px solid var(--rule);height:22px}
.sig{display:flex;align-items:flex-end;font-size:11px;height:22px}
.sig .line{border-bottom:1px solid var(--rule);height:12px}
.sig-note{font-size:8.5px;font-style:italic;text-align:right;margin-top:4px;margin-right:20px}
.footer{position:absolute;left:0;right:0;top:464px;text-align:center;color:var(--navy);font-weight:700;font-size:13px;line-height:20px}
.footer .call{font-style:italic}
</style>
</head>
<body>
<main class="sheet">

  <section class="voucher">
    <div class="wave wave-left" role="img" aria-label="Blue guilloche line pattern"></div>
    <div class="wave wave-right" role="img" aria-label="Blue guilloche line pattern"></div>
    <div class="brand-tab"><span class="dot"></span><span class="name">Sunbreak Getaways</span></div>

    <div class="panel panel-left">
      <div class="bar">Attraction Ticket Voucher</div>
      <p class="center offer">Present This Voucher at our Welcome Center for:<br>Two tickets to Copper Lantern Supper &amp; Show of Orlando, FL</p>
      <p class="note">* Addition Guests may pre-pay/purchase additional tickets at our current rate:<br>Currently $27.00 each. Retail Value per ticket is $62.00</p>
      <div class="package">Package #: <span class="box"></span></div>
      <div class="bar">Ticket Holder Information</div>
      <div class="fields">
        <div class="field">Primary Guest:<span class="line"></span></div>
        <div class="field">Second Guest:<span class="line"></span></div>
        <div class="field">Third Guest:<span class="line"></span></div>
        <div class="field">Fourth Guest:<span class="line"></span></div>
        <div class="field">Address:<span class="line"></span></div>
        <div class="field">City:<span class="line"></span>State:<span class="line short"></span>Zip:<span class="line short"></span></div>
        <div class="field">Day Ph: (<span class="line tiny"></span>)<span class="line"></span>Evening Ph: (<span class="line tiny"></span>)<span class="line"></span></div>
      </div>
    </div>

    <div class="panel panel-right">
      <div class="bar">Attraction Date of Interest</div>
      <p class="center" style="margin-top:8px">Reservation Form must be received at least 60 days prior to your earliest requested arrival date.<br>or Call for reservation: 1-888-555-0147</p>
      <div class="interest">
        <div class="attraction-mark">Copper Lantern Supper</div>
        <div class="interest-copy">
          <p class="title">Attraction Date of Interest</p>
          <div class="line"></div>
          <p class="hint">MM/DD/YY</p>
        </div>
      </div>
      <div class="extra">Additional (Required by/Request):<span class="line"></span></div>
      <div class="extra-line"></div>
      <div class="bar" style="margin-top:26px">Required to Process</div>
      <p class="center" style="font-size:11px;line-height:14px;margin-top:8px">I/We have read and understand fully all the Terms and Condition of this Attraction, as distinguished on this Attraction Ticket Voucher.</p>
      <div class="sig" style="margin-top:20px">Signature:&nbsp;<span class="line" style="width:130px"></span>Date:<span class="line" style="flex:1"></span></div>
      <p class="sig-note">Required for Processing reservation Request.</p>
      <div class="sig" style="margin-top:6px">Signature:&nbsp;<span class="line" style="flex:1"></span></div>
    </div>

    <div class="footer">
      <p>SEND FORM TO: ATTN Shipping Dept.</p>
      <p>2200 Harbor Light Parkway, Coral Bay, FL 33400 USA</p>
      <p class="call">Or simply call to confirm 1-888-555-0147 Option #1</p>
    </div>
  </section>

  <section class="voucher">
    <div class="wave wave-left" role="img" aria-label="Blue guilloche line pattern"></div>
    <div class="wave wave-right" role="img" aria-label="Blue guilloche line pattern"></div>
    <div class="brand-tab"><span class="dot"></span><span class="name">Sunbreak Getaways</span></div>

    <div class="panel panel-left">
      <div class="bar">Attraction Ticket Voucher</div>
      <p class="center offer">Present This Voucher at our Welcome Center for:<br>Two tickets to Copper Lantern Supper &amp; Show of Orlando, FL</p>
      <p class="note">* Addition Guests may pre-pay/purchase additional tickets at our current rate:<br>Currently $27.00 each. Retail Value per ticket is $62.00</p>
      <div class="package">Package #: <span class="box"></span></div>
      <div class="bar">Ticket Holder Information</div>
      <div class="fields">
        <div class="field">Primary Guest:<span class="line"></span></div>
        <div class="field">Second Guest:<span class="line"></span></div>
        <div class="field">Third Guest:<span class="line"></span></div>
        <div class="field">Fourth Guest:<span class="line"></span></div>
        <div class="field">Address:<span class="line"></span></div>
        <div class="field">City:<span class="line"></span>State:<span class="line short"></span>Zip:<span class="line short"></span></div>
        <div class="field">Day Ph: (<span class="line tiny"></span>)<span class="line"></span>Evening Ph: (<span class="line tiny"></span>)<span class="line"></span></div>
      </div>
    </div>

    <div class="panel panel-right">
      <div class="bar">Attraction Date of Interest</div>
      <p class="center" style="margin-top:8px">Reservation Form must be received at least 60 days prior to your earliest requested arrival date.<br>or Call for reservation: 1-888-555-0147</p>
      <div class="interest">
        <div class="attraction-mark">Maple grove Laugh House</div>
        <div class="interest-copy">
          <p class="title">Attraction Date of Interest</p>
          <div class="line"></div>
          <p class="hint">MM/DD/YY</p>
        </div>
      </div>
      <div class="extra">Additional (Required by/Request):<span class="line"></span></div>
      <div class="extra-line"></div>
      <div class="bar" style="margin-top:26px">Required to Process</div>
      <p class="center" style="font-size:11px;line-height:14px;margin-top:8px">I/We have read and understand fully all the Terms and Condition of this Attraction, as distinguished on this Attraction Ticket Voucher.</p>
      <div class="sig" style="margin-top:20px">Signature:&nbsp;<span class="line" style="width:130px"></span>Date:<span class="line" style="flex:1"></span></div>
      <p class="sig-note">Required for Processing reservation Request.</p>
      <div class="sig" style="margin-top:6px">Signature:&nbsp;<span class="line" style="flex:1"></span></div>
    </div>

    <div class="footer">
      <p>SEND FORM TO: ATTN Shipping Dept.</p>
      <p>2200 Harbor Light Parkway, Coral Bay, FL 33400 USA</p>
      <p class="call">Or simply call to confirm 1-888-555-0147 Option #1</p>
    </div>
  </section>

</main>
</body>
</html>
```